Gestaltung einer Eyecatcher Grafik
Zielgruppe
Zum einen handelt es sich um Kunden aus dem familiären / bürgerlichen Kontext, also Eltern aber auch kinderlose Paare. Bei ersteren liegt der Fokus auf personalisierbaren Kinderprodukten, also Klei-dung, Spielzeug, Mobilität. Die zweite Gruppe, also kinderlose Paare, interessiert sich für die Ausstattung ihrer Wohnung oder ihres Hauses.
Zum anderen sprechen wir Singles an, die noch im Studium oder der Ausbildung stehen. Altersschwerpunkt unter 30 Jahre, gehobenes Bildungsniveau. Sie wollen "ihr eigenes Ding" machen und suchen beim Konsumieren etwas Besonderes.
Neben diesen Kundengruppen sollen insbesondere Designer angesprochen werden, die Ihre kreativen Arbeiten in unserem Designkatalog platzieren und durch die Platzierung auf den Produkten vermarkten.
Aufgabenstellung
Wir möchten eine Ergänzung unseres Website-Layouts vornehmen. Dazu soll auf www.torvela.de ein Eyecatcher zwischen dem horizontalen Menü und der Contentbox auf der Startseite eingefügt werden, der das Prinzip von Torvela erklärt.
Auf unserer Plattform kann jeder Kunde alle angebotenen Produkte selbst gestalten und kaufen. Der Eyecatcher hat zwei Ziele:
1. gleichzeitig müssen wir dem Kunden vermitteln, dass er alle Produkte auf Torvela selbst gestalten kann. Das ist das Alleinstellungsmerkmal unseres Marktplatzes.
2. wir müssen etwas mehr "Human Touch" auf die Seite bringen
Es sollte also eine Mischung aus Text und Grafik sein. Vielfalt und Einzigartigkeit sollte zum Ausdruck kommen. Eine menschliche Motivkomponente wäre nicht schlecht. Der Slogan "Lebe Deinen Style" kann, muss aber nicht zum Einsatz kommen. Wenn Sie eine Idee zu einem alternativen Slogan haben, bin ich gespannt!
Viele Grüße!

```html
<!DOCTYPE html>
<html lang="de">
<head>
<meta charset="utf-8">
<title>Torvela – Gestalte Deine Produkte</title>
<link rel="stylesheet" href="https://fonts.googleapis.com/css2?family=Open+Sans:wght@400;600;700&display=swap">
<style>
:root{
  --header-top:#5e5f63;
  --header-bottom:#434447;
  --accent-orange:#d9532a;
  --accent-orange-dark:#c2441c;
  --green:#7ea52b;
  --green-light:#a6cf4a;
  --green-banner-a:#8cc43c;
  --green-banner-b:#b5da63;
  --text-dark:#444549;
  --text-mid:#606165;
  --page-bg:#f5f5f5;
  --card-border:#dcdcdc;
  --white:#ffffff;
}
*{margin:0;padding:0;box-sizing:border-box}
html,body{width:1200px;height:927px;overflow:hidden;background:var(--page-bg)}
body{font-family:"Open Sans",Arial,sans-serif;color:var(--text-dark)}
.stage{position:absolute;left:0;top:0;width:1100px;height:850px;transform:scale(1.0909);transform-origin:0 0;
  background:linear-gradient(#e6e6e6 70px,#f7f7f7 160px,#f7f7f7)}
.abs{position:absolute}

/* header */
.topbar{left:0;top:0;width:1100px;height:66px;background:linear-gradient(var(--header-top),var(--header-bottom))}
.topbar-line{left:0;top:66px;width:1100px;height:5px;background:var(--accent-orange)}
.brand{left:83px;top:0;width:197px;height:84px;background:var(--white);border-radius:0 0 6px 6px;
  box-shadow:0 2px 5px rgba(0,0,0,.35);z-index:3;display:flex;align-items:center;justify-content:center}
.brand-name{font-size:32px;font-weight:700;color:var(--green);line-height:34px;letter-spacing:.5px}
.main-nav a{position:absolute;top:27px;font-size:13px;color:var(--white);text-decoration:none}
.cart{left:810px;top:8px;width:203px;height:48px;border:1px solid #6e6f73;border-radius:3px;background:rgba(0,0,0,.1)}
.cart svg{position:absolute;left:10px;top:11px}
.cart-sep{position:absolute;left:46px;top:6px;width:1px;height:34px;background:#77787c}
.cart-info{position:absolute;left:53px;top:6px;color:var(--white);font-size:9px;line-height:10px}
.cart-info b{display:block;font-size:12px;line-height:13px}
.checkout{position:absolute;left:154px;top:8px;width:42px;height:31px;background:var(--green-light);
  color:var(--white);font-size:9px;font-weight:700;text-align:center;line-height:11px;padding-top:4px}

/* eyecatcher */
.hero{left:67px;top:70px;width:946px;height:138px;border-radius:0 0 6px 6px;overflow:hidden;
  background:linear-gradient(90deg,var(--green-banner-a),var(--green-banner-b) 70%,#9fcf4e)}
.hero-tag{left:0;top:26px;height:31px;width:111px;background:var(--accent-orange);color:var(--white);
  font-size:19px;font-weight:700;line-height:31px;text-align:center}
.hero-title{left:118px;top:26px;font-size:19px;font-weight:700;color:var(--white);line-height:31px}
.hero-text{left:16px;top:68px;width:486px;font-size:13px;line-height:17px;color:var(--white)}
.hero-photo{left:560px;top:0;width:260px;height:138px;
  background:radial-gradient(ellipse at 60% 55%,#b88a6a 0,#8f6450 35%,rgba(140,196,60,0) 70%)}
.hero-cta{left:812px;top:22px;width:117px;height:99px;background:var(--white);border-radius:3px;
  box-shadow:0 2px 4px rgba(0,0,0,.3);overflow:hidden;text-align:center}
.hero-cta p{font-size:15px;font-weight:700;color:var(--text-mid);line-height:18px;padding-top:9px}
.hero-cta a{position:absolute;left:0;bottom:0;width:117px;height:28px;background:var(--accent-orange);
  color:var(--white);font-size:15px;font-weight:700;line-height:28px;text-decoration:none}

.welcome{left:0;top:218px;width:1080px;text-align:center;font-size:19.5px;font-weight:700;color:var(--text-mid)}
.welcome span{color:var(--accent-orange)}

/* content */
.content{left:67px;top:254px;width:946px;height:479px;background:var(--white);border:1px solid var(--card-border);border-radius:6px}
.catalog{left:92px;top:273px;width:205px;height:331px;border:1px solid var(--card-border);border-radius:5px;overflow:hidden}
.catalog h2{height:38px;background:linear-gradient(#646569,#4a4b4f);color:var(--white);font-size:16px;
  font-weight:600;line-height:38px;padding-left:36px}
.catalog ul{list-style:none;padding:15px 0 0 35px}
.catalog li{font-size:15px;font-weight:600;line-height:27px}
.catalog li a{color:var(--green);text-decoration:underline}
.all-products{position:absolute;left:32px;top:269px;width:138px;height:31px;border-radius:4px;
  background:linear-gradient(var(--green-light),var(--green));color:var(--white);font-size:16px;font-weight:700;
  text-align:center;line-height:31px;text-decoration:none}

.section-title{left:327px;top:272px;font-size:15px;font-weight:600;color:var(--text-dark)}
.steps{left:327px;top:311px}
.topseller{left:327px;top:378px;font-size:14px;font-weight:600;color:var(--text-dark)}
.topseller span{font-size:16.5px;color:var(--accent-orange)}
.pager{left:925px;top:380px;font-size:14px;color:var(--green)}
.pager b{margin-right:8px}.pager a{color:var(--green);text-decoration:none;margin-right:8px}

.product{top:414px;width:205px;height:186px;border:1px solid var(--card-border);border-radius:5px;text-align:center}
.product-image{width:175px;height:145px;margin:14px auto 0}
.product-name{font-size:13px;color:var(--green);margin-top:3px;letter-spacing:.2px}

/* footer */
.footer-line{left:67px;top:750px;width:946px;height:1px;background:#d4d4d4}
.social{top:768px;display:flex;align-items:center;gap:5px;font-size:12.5px;color:var(--text-dark)}
.social i{display:block;width:24px;height:24px;background:var(--green);border-radius:4px}
.footer-nav{left:640px;top:766px;font-size:13px}
.footer-nav a{color:var(--green);text-decoration:none;padding:0 9px;border-left:1px solid #cfcfcf}
.footer-nav a:first-child{border-left:0}
.footer-brand{left:912px;top:792px;font-size:17px;font-weight:700;color:#8a8b8f}
</style>
</head>
<body>
<div class="stage">
  <div class="abs topbar"></div>
  <div class="abs topbar-line"></div>

  <div class="abs brand">
    <div class="brand-name">Torvela</div>
  </div>

  <nav class="main-nav">
    <a href="#" style="left:307px">Produkte</a>
    <a href="#" style="left:400px">Mein Torvela</a>
    <a href="#" style="left:511px">Kontakt</a>
  </nav>

  <div class="abs cart">
    <svg width="28" height="24" viewBox="0 0 28 24" fill="none" stroke="#fff" stroke-width="1.6">
      <path d="M1 2h4l3 14h15l3-10H7"/>
      <path d="M9 9h16M10 13h13M13 6v10M18 6v10"/>
      <circle cx="10" cy="20" r="2"/><circle cx="21" cy="20" r="2"/>
    </svg>
    <div class="cart-sep"></div>
    <div class="cart-info">0 Artikel<b>0,00 €</b>zzgl. Versand</div>
    <div class="checkout">ZUR<br>KASSE</div>
  </div>

  <section class="abs hero">
    <div class="abs hero-photo" role="img" aria-label="Foto eines lachenden jungen Paares"></div>
    <div class="abs hero-tag">Produkte</div>
    <div class="abs hero-title">so außergewöhnlich wie du selber....</div>
    <p class="abs hero-text">hier könnte dann noch mehr text stehen der das System erklärt und die Kunden auf besonderheiten hinweißt... hier könnte dann noch mehr text stehen der das System erklärt und die Kunden auf besonderheiten hinweißt...</p>
    <div class="abs hero-cta">
      <p>Dein Produkt<br>jetzt selber<br>gestalten</p>
      <a href="#">Los gehts ›</a>
    </div>
  </section>

  <h1 class="abs welcome"><span>Willkommen auf Torvela -</span> Gestalte Deine Produkte ganz einfach selbst.</h1>

  <div class="abs content"></div>

  <aside class="abs catalog">
    <h2>KATALOG</h2>
    <ul>
      <li><a href="#">Accessoires</a></li>
      <li><a href="#">Bekleidung</a></li>
      <li><a href="#">Büro</a></li>
      <li><a href="#">Geschenke</a></li>
    </ul>
    <a class="all-products" href="#">alle Produkte</a>
  </aside>

  <h3 class="abs section-title">Gestalte jetzt Dein Produkt:</h3>

  <svg class="abs steps" width="642" height="36" viewBox="0 0 642 36" font-family="Open Sans, Arial, sans-serif">
    <defs>
      <linearGradient id="step-one" x1="0" x2="1"><stop offset="0" stop-color="#8d8e92"/><stop offset=".6" stop-color="#4b4c50"/><stop offset="1" stop-color="#3f4043"/></linearGradient>
      <linearGradient id="step-two" x1="0" x2="1"><stop offset="0" stop-color="#c9e19a"/><stop offset="1" stop-color="#7ea52b"/></linearGradient>
      <linearGradient id="step-three" x1="0" x2="1"><stop offset="0" stop-color="#efb59c"/><stop offset=".6" stop-color="#d9532a"/><stop offset="1" stop-color="#c2441c"/></linearGradient>
    </defs>
    <path d="M5 0H444L462 18L444 36H5Q0 36 0 31V5Q0 0 5 0Z" fill="url(#step-three)"/>
    <path d="M200 0H432L450 18L432 36H200Z" fill="url(#step-two)"/>
    <path d="M5 0H212L230 18L212 36H5Q0 36 0 31V5Q0 0 5 0Z" fill="url(#step-one)"/>
    <path d="M444 0H637Q642 0 642 5V31Q642 36 637 36H444L462 18Z" fill="#c9461d"/>
    <g fill="#3f4043"><rect x="12" y="8" width="20" height="20" rx="5" fill="#6a6b6f"/><rect x="242" y="8" width="20" height="20" rx="5"/><rect x="460" y="8" width="20" height="20" rx="5"/></g>
    <g font-size="12" font-weight="700" fill="#fff" text-anchor="middle"><text x="22" y="23">1</text><text x="252" y="23">2</text><text x="470" y="23">3</text></g>
    <g font-size="17" font-weight="600" fill="#fff"><text x="53" y="24">Produkt wählen</text><text x="283" y="24">Produkt gestalten</text><text x="518" y="24">Bestellen</text></g>
  </svg>

  <h3 class="abs topseller"><span>TOPSELLER</span> aus unserem Katalog</h3>
  <div class="abs pager"><b>1</b><a href="#">2</a><a href="#">3</a></div>

  <article class="abs product" style="left:327px">
    <div class="product-image" role="img" aria-label="Notebooktasche mit bunter Graffiti-Illustration" style="background:linear-gradient(135deg,#f2f2f2,#c8c8c8 45%,#e8a64a 65%,#f4f4f4)"></div>
    <div class="product-name">Easy Flap Notebooktasche</div>
  </article>
  <article class="abs product" style="left:547px">
    <div class="product-image" role="img" aria-label="Foto eines silbernen Schlüsselanhängers mit Schmetterlingsmotiv" style="background:radial-gradient(ellipse at 50% 55%,#d8d8d8 0,#8a8a8a 30%,#222 65%)"></div>
    <div class="product-name">Photo-Schlüsselanhänger</div>
  </article>
  <article class="abs product" style="left:767px">
    <div class="product-image" role="img" aria-label="Halskette mit rundem Motivanhänger und Anker" style="background:radial-gradient(circle at 50% 50%,#f1eee6 0,#d7d3ca 30%,#fff 60%)"></div>
    <div class="product-name">Kette Anker</div>
  </article>

  <div class="abs footer-line"></div>
  <div class="abs social" style="left:88px"><i></i>Chirpline</div>
  <div class="abs social" style="left:186px"><i></i>The Blog</div>
  <nav class="abs footer-nav">
    <a href="#">Home</a><a href="#">Kontakt</a><a href="#">Impressum</a><a href="#">AGB</a><a href="#">Datenschutz</a>
  </nav>
  <div class="abs footer-brand">Torvela</div>
</div>
</body>
</html>
```